Startup company business card (Media & Advertising)

we need a business card design for a company that is a startup in the media and aggregation industry. Card needs to look funky and of a new breed/modern and upmarket.

Target Market(s)

advertisers/ brand agencies & media publishers

Industry/Entity Type

Advertising

Contact Information for Business Card

Please ensure the front face signifies our brand (plintovo.com) and back has details for the contact. Standard contact such as phone , address, email , website etc.

Font styles to use
Other font styles liked:
• use styleguide and logo font and color

Colors

Designer to choose colors to be used in the design.

Requirements
Must have
• We are disrupting the media and agency industry so subtlety would be good to use imagery to signify this
Nice to have
• Please use logo colors for branding
Should not have
• be as creative and provide few options. Pick a brand color from logo and styleguide

```html
<!DOCTYPE html>
<html lang="en">
<head>
<meta charset="utf-8">
<title>plintovo business card</title>
<link rel="stylesheet" href="https://fonts.googleapis.com/css2?family=Arvo:wght@400;700&display=swap">
<style>
  :root {
    --backdrop: #c9c9c9;
    --brand-red: #e8343f;
    --brand-red-deep: #c8283f;
    --ink-black: #0e0e0e;
    --paper-white: #ffffff;
  }
  * { margin: 0; padding: 0; box-sizing: border-box; }
  html, body { width: 1200px; height: 802px; overflow: hidden; }
  body {
    background: var(--backdrop);
    font-family: "Arvo", Georgia, serif;
    position: relative;
  }
  .card {
    position: absolute;
    top: 274px;
    width: 443px;
    height: 265px;
    overflow: hidden;
    box-shadow: 2px 3px 5px rgba(0,0,0,0.35);
  }
  .card--contact {
    left: 136px;
    background: linear-gradient(100deg, var(--brand-red) 0%, var(--brand-red-deep) 45%, var(--brand-red) 100%);
    color: var(--paper-white);
  }
  .card--brand {
    left: 624px;
    background: var(--ink-black);
  }
  .edge-band {
    position: absolute;
    top: 0; right: 0;
    width: 110px; height: 265px;
  }
  .person { position: absolute; left: 20px; top: 32px; }
  .person__name { font-weight: 700; font-size: 15.5px; line-height: 18px; }
  .person__role { font-size: 12.5px; line-height: 15px; }
  .contact-list { position: absolute; left: 20px; top: 144px; list-style: none; }
  .contact-list li {
    display: flex; align-items: center; gap: 3px;
    font-size: 12px; line-height: 16.5px;
  }
  .contact-list svg { width: 13px; height: 13px; flex: none; }
  .address { position: absolute; left: 21px; top: 203px; font-size: 12px; line-height: 16px; }
  .wordmark {
    position: absolute; left: 52px; top: 100px;
    display: flex; align-items: center; gap: 34px;
  }
  .wordmark__dot {
    width: 62px; height: 62px; border-radius: 50%;
    background: var(--brand-red);
  }
  .wordmark__name {
    font-weight: 700; font-size: 42px; color: var(--paper-white);
    letter-spacing: 0.5px;
  }
</style>
</head>
<body>
  <section class="card card--contact">
    <svg class="edge-band" viewBox="0 0 110 265" aria-hidden="true">
      <path d="M110 0 L96 0 C 82 30, 80 70, 84 110 C 88 160, 60 215, 20 265 L110 265 Z" fill="var(--ink-black)"/>
    </svg>
    <div class="person">
      <p class="person__name">Marcus Hale</p>
      <p class="person__role">Managing Director</p>
    </div>
    <ul class="contact-list">
      <li>
        <svg viewBox="0 0 14 14" aria-hidden="true"><rect x="0.7" y="0.7" width="12.6" height="12.6" rx="2" fill="none" stroke="#fff" stroke-width="1.2"/><path d="M4 3.5 L5.6 3.5 L6.2 5.4 L5.3 6.2 C5.8 7.4 6.6 8.2 7.8 8.7 L8.6 7.8 L10.5 8.4 L10.5 10 C7 10.3 3.7 7 4 3.5 Z" fill="#fff"/></svg>
        044-987 210 346
      </li>
      <li>
        <svg viewBox="0 0 14 14" aria-hidden="true"><rect x="0.7" y="2.5" width="12.6" height="9" fill="none" stroke="#fff" stroke-width="1.2"/><path d="M0.7 2.5 L7 8 L13.3 2.5" fill="none" stroke="#fff" stroke-width="1.2"/></svg>
        hello@plintovo.com
      </li>
      <li>
        <svg viewBox="0 0 14 14" aria-hidden="true"><g fill="none" stroke="#fff" stroke-width="1.1"><circle cx="7" cy="7" r="6.2"/><ellipse cx="7" cy="7" rx="2.8" ry="6.2"/><path d="M0.8 7 H13.2 M1.8 3.8 H12.2 M1.8 10.2 H12.2"/></g></svg>
        www.plintovo.com
      </li>
    </ul>
    <p class="address">58, Meridian Lane East<br>Portvale City, 30817</p>
  </section>

  <section class="card card--brand">
    <div class="wordmark">
      <span class="wordmark__dot" aria-hidden="true"></span>
      <span class="wordmark__name">plintovo</span>
    </div>
  </section>
</body>
</html>
```